CEDARWICK RESTASURANT WINE LIST - REDESIGN/REFORMAT

Need a menu redesign/resizing of our wine list/beverage menu from standard letter size to a 4.25 x 11 inch “Drink Menu” size. Could do with a nicer cover page. Wine list, descriptions, pricing, almost all stays the same minus the formatting and possibly new cover page/font.

Few minor edits need to be made to descriptions and pricing on wine and beer list.

Someone competent in illustrator should be able to get this done in literal hours, and I don’t find myself having the time, and less know how than someone here!

Need sent back in PDF Format so i can send to local print shop.

Thanks in advance

Target Market(s)

Our restaurants's customers/patrons

Colors

Designer to choose only greyscale colors for use in the design.

Requirements
Must have
• A few text edits sent in before final edit. please PM so i can tell you what aspects of the wine list/beer menu need to be edited.
Nice to have
• Elegant font but readable

```html
<!DOCTYPE html>
<html lang="en">
<head>
<meta charset="utf-8">
<title>Cedarwick Restaurant – Wine List</title>
<link rel="stylesheet" href="https://fonts.googleapis.com/css2?family=Cormorant+Garamond:wght@500&family=Crimson+Text:ital,wght@0,400;0,600;1,400;1,600;1,700&family=Jost:wght@400&display=swap">
<style>
:root{
  --page:#e9e9e9;
  --paper:#ffffff;
  --cover:#f2f2f2;
  --ink:#1c1c1c;
  --soft:#4a4a4a;
  --rule:#9a9a9a;
  --scene-top:#f4f4f4;
  --scene-mid:#cfcfcf;
  --scene-low:#9c9c9c;
}
*{margin:0;padding:0;box-sizing:border-box}
html,body{width:1200px;height:769px;overflow:hidden;background:var(--page)}
body{position:relative;font-family:"Crimson Text",serif;color:var(--ink)}
.panel{position:absolute;top:15px;width:286px;height:740px;background:var(--paper);overflow:hidden}
.p1{left:16px;background:var(--cover)}
.p2{left:309px}.p3{left:602px}.p4{left:895px}

/* cover */
.cover-frame{position:absolute;left:15px;top:15px;width:257px;height:300px;border:1px solid var(--rule);border-bottom:none}
.brand{position:absolute;left:0;right:0;top:52px;text-align:center;font-family:"Cormorant Garamond",serif;font-weight:500;color:var(--ink);line-height:1;letter-spacing:.5px}
.brand-name{display:block;font-size:32px}
.brand-sub{display:block;font-size:32px;margin-top:2px}
.cover-title{position:absolute;left:0;right:0;top:180px;text-align:center;font-family:"Jost",sans-serif;font-weight:400;font-size:40px;letter-spacing:1px;color:var(--ink)}
.cover-scene{position:absolute;left:0;top:293px;width:286px;height:447px;background:linear-gradient(180deg,var(--cover) 0%,var(--scene-top) 8%,var(--scene-mid) 28%,#e2e2e2 40%,var(--scene-mid) 60%,var(--scene-low) 100%)}

/* menu panels */
.panel-title{position:absolute;left:0;right:0;top:32px;text-align:center;font-style:italic;font-weight:600;font-size:20px;line-height:1.1}
.col-heads{position:absolute;top:87px;right:12px;display:grid;grid-template-columns:34px 36px;font-size:9.5px;text-align:right}
.section{position:absolute;left:17px;right:12px}
.cat{font-style:italic;font-weight:600;font-size:13px;line-height:14px}
.item{margin:0 0 15px 9px}
.item-row{display:grid;grid-template-columns:minmax(0,1fr) 28px 38px;font-size:8.4px;line-height:11px;white-space:nowrap}
.item-row.tight{font-size:7.9px;letter-spacing:-.1px}
.item-row .g,.item-row .b{text-align:right;font-size:8.4px}
.note{font-style:italic;font-size:6.2px;line-height:8px;color:var(--soft)}
.footer{position:absolute;left:0;right:0;top:692px;text-align:center;font-weight:700;font-size:7.2px;line-height:10px}
.footer em{font-style:italic}

/* drinks panel */
.p4 .panel-title{top:24px;line-height:24px}
.head-row{display:grid;grid-template-columns:1fr 52px 46px;align-items:baseline}
.head-row span{font-size:9.5px;text-align:right}
.sub{font-style:italic;font-weight:700;font-size:8px;line-height:11px;margin-left:9px}
.line{display:grid;grid-template-columns:1fr 30px;margin-left:9px;font-size:6.6px;line-height:8.5px;margin-bottom:5px}
.line .b{text-align:right;font-size:8.4px}
.line i{color:var(--soft)}
.pair{display:grid;grid-template-columns:1fr 52px 46px;margin-left:9px;font-size:8.4px;line-height:11px}
.pair span{text-align:right}
.pair .nm{text-align:left;font-style:italic;font-weight:700;font-size:7.6px}
.simple{display:grid;grid-template-columns:1fr 30px;margin-left:9px;font-size:6.6px;line-height:13.5px}
.simple .b{text-align:right;font-size:8.4px}
</style>
</head>
<body>

<section class="panel p1">
  <div class="cover-frame"></div>
  <div class="brand"><span class="brand-name">CEDARWICK</span><span class="brand-sub">RESTAURANT</span></div>
  <h1 class="cover-title">WINE LIST</h1>
  <div class="cover-scene" role="img" aria-label="Sketched seaside illustration of a wine bottle and a glass of red wine on a deck railing"></div>
</section>

<section class="panel p2">
  <h2 class="panel-title">White Wines &amp; Bubbles</h2>
  <div class="col-heads"><span>Glass</span><span>Bottle</span></div>

  <div class="section" style="top:87px">
    <h3 class="cat">Chardonnay</h3>
    <div class="item"><div class="item-row"><span>2023 Harlow Ridge - Sonoma - California</span><span class="g">$10</span><span class="b">$38</span></div><p class="note">Pear &amp; green apple with splashes of vanilla &amp; spice.</p></div>
    <div class="item"><div class="item-row"><span>2024 Thomas Reade - Lodi - California</span><span class="g"></span><span class="b">$44</span></div><p class="note">Elegant &amp; crisp. Peach &amp; white currant flavors. Creamy finish.</p></div>
  </div>

  <div class="section" style="top:165px">
    <h3 class="cat">Moscato</h3>
    <div class="item"><div class="item-row"><span>2024 Corvel - Rogue Valley - Oregon</span><span class="g">$9</span><span class="b">$34</span></div><p class="note">Aromas of white peach, Asian pear, honeysuckle &amp;<br>citrus blossom with crisp acidity. Delicate &amp; delicious.</p></div>
    <div class="item"><div class="item-row"><span>2021 Moscato D'Asti - Paolo Verri - Italy - 375ml</span><span class="g"></span><span class="b">$30</span></div><p class="note">Fragrant fruity bouquet. Musky notes. Light &amp; gentle on the palate.</p></div>
  </div>

  <div class="section" style="top:251px">
    <h3 class="cat">Pinot Grigio</h3>
    <div class="item"><div class="item-row"><span>2024 Lunetta - Friuli Grave - Italy</span><span class="g">$10</span><span class="b">$38</span></div><p class="note">Floral notes. Pear and banana flavors. Crisp and delicate.</p></div>
  </div>

  <div class="section" style="top:295px">
    <h3 class="cat">Riesling</h3>
    <div class="item"><div class="item-row"><span>2023 Corvel - Rogue Valley - Oregon</span><span class="g">$9</span><span class="b">$34</span></div><p class="note">Aromas of lavender, dried rose petal &amp; green apple with nectarine flavor.<br>Generous texture with a lingering finish.</p></div>
  </div>

  <div class="section" style="top:349px">
    <h3 class="cat">Rosé</h3>
    <div class="item"><div class="item-row"><span>2024 Endless June - Southern Rhone - France</span><span class="g">$8</span><span class="b">$30</span></div><p class="note">Aroma of ripe cherry. Flavors of apricot, vanilla &amp; strawberry.<br>Smooth &amp; Refreshing. Blend of Grenache, Syrah &amp; Clairette.</p></div>
  </div>

  <div class="section" style="top:403px">
    <h3 class="cat">Sauvignon Blanc</h3>
    <div class="item"><div class="item-row"><span>2025 Fernbrook - Redwood Valley - California</span><span class="g">$9</span><span class="b">$34</span></div><p class="note">Pear flavor with a hint of herbs.</p></div>
    <div class="item"><div class="item-row"><span>2024 Alvaro - Mendocino - California</span><span class="g"></span><span class="b">$48</span></div><p class="note">Citrus note with gooseberry flavor.</p></div>
    <div class="item"><div class="item-row"><span>2022 Mt. Serene - North Canterbury - New Zealand</span><span class="g"></span><span class="b">$42</span></div><p class="note">Flavors of tropical fruits. Pineapple &amp; Guava Aromas. Creamy.</p></div>
  </div>

  <div class="section" style="top:512px">
    <h3 class="cat">Champagnes &amp; Sparkling Wines</h3>
    <div class="item"><div class="item-row"><span>Amore Mio - Prosecco - Brut - Italy</span><span class="g">$10</span><span class="b">$38</span></div><p class="note">Extremely refreshing.<br>Elegant &amp; Fruity with sweet peach &amp; apple flavors.</p></div>
    <div class="item"><div class="item-row tight" style="grid-template-columns:minmax(0,1fr) 0 30px"><span>Henri Vogel - Brut Reserve - Cremant De Alsace - France</span><span class="g"></span><span class="b">$42</span></div><p class="note">Blend of Auxerrois &amp; Pinot Blanc. White peach aroma.<br>Flavors of Asian pear, brioche &amp; rich honey.</p></div>
    <div class="item"><div class="item-row"><span>2017 Opal Crossing - Blanc de Blanc - California</span><span class="g"></span><span class="b">$66</span></div><p class="note">100% Chardonnay. Flavors of strawberry &amp; kiwi, green apple peel.</p></div>
    <div class="item"><div class="item-row"><span>2020 Ravensberg - Brut Rosé - Calistoga - California</span><span class="g"></span><span class="b">$78</span></div></div>
  </div>

  <p class="footer"><em>Enjoy 50% off bottled wines and sakes every Wednesday.</em><br>Bottle vintage subject to change.&nbsp; Corkage Fee: $15 per bottle<br>For each bottle purchased from our wine list,<br>we will waive one corkage fee.</p>
</section>

<section class="panel p3">
  <h2 class="panel-title">Red Wines</h2>
  <div class="col-heads"><span>Glass</span><span>Bottle</span></div>

  <div class="section" style="top:87px">
    <h3 class="cat">Barbera</h3>
    <div class="item"><div class="item-row"><span>2023 Montalbi - Granite Hill Ranch<br>- Amador County - California</span><span class="g"></span><span class="b">$62</span></div><p class="note">Layer after layer of dark fruits, exotic spices &amp; truffles.<br>Smooth and well balanced.</p></div>
  </div>

  <div class="section" style="top:157px">
    <h3 class="cat">Cabernet Sauvignon</h3>
    <div class="item" style="margin-bottom:6px"><div class="item-row"><span>2022 Daniel Kurtz - North Coast - California</span><span class="g">$11</span><span class="b">$42</span></div><p class="note">Flavors of dark cherry, vanilla &amp; espresso.<br>Smooth and light tannins.</p></div>
    <div class="item" style="margin-bottom:6px"><div class="item-row"><span>2021 Fernbrook - Mendocino - California</span><span class="g"></span><span class="b">$75</span></div><p class="note">Black cherry &amp; cedar aromas. Balanced oak profile.</p></div>
    <div class="item"><div class="item-row"><span>2021 Hollis Brandt - Sonoma Valley - California</span><span class="g"></span><span class="b">$78</span></div><p class="note">Aromas of black currant &amp; blueberry laced with vanilla.</p></div>
  </div>

  <div class="section" style="top:259px">
    <h3 class="cat">Merlot</h3>
    <div class="item"><div class="item-row"><span>2022 Harlow Ridge - Sonoma California</span><span class="g">$10</span><span class="b">$38</span></div><p class="note">Flavors of black cherry, blackberry, and plum.<br>Rich, concentrated, and silky.</p></div>
  </div>

  <div class="section" style="top:314px">
    <h3 class="cat">Pinotage</h3>
    <div class="item"><div class="item-row"><span>2013 Opal Crossing - Trinidad - California</span><span class="g"></span><span class="b">$48</span></div><p class="note">Aromas of black currant &amp; raspberry complement flavors of<br>chocolate &amp; pomegranate.</p></div>
  </div>

  <div class="section" style="top:371px">
    <h3 class="cat">Pinot Noir</h3>
    <div class="item" style="margin-bottom:11px"><div class="item-row"><span>2021 Shell Point - Edna Valley - California</span><span class="g">$10</span><span class="b">$38</span></div><p class="note">Aromas of strawberry &amp; wild raspberries.<br>Smooth &amp; well balanced with creamy &amp; caramel finish.</p></div>
    <div class="item"><div class="item-row"><span>2023 Alvaro - Mendocino - California</span><span class="g"></span><span class="b">$68</span></div><p class="note">A potpourri of black cherry, raspberry &amp; toasty oak with a balanced tannins.</p></div>
  </div>

  <div class="section" style="top:458px">
    <h3 class="cat">Zinfandel</h3>
    <div class="item" style="margin-bottom:10px"><div class="item-row"><span>2022 Sideshow - Lodi - California</span><span class="g">$9</span><span class="b">$34</span></div><p class="note">Flavors of blackberries, vanilla &amp; cherries. Medium body and smooth finish.</p></div>
    <div class="item"><div class="item-row"><span>2023 Bellavio - Sonoma County - California</span><span class="g"></span><span class="b">$46</span></div><p class="note">Bold blackberry &amp; licorice aromas.<br>Well structured black cherry, smoky pepper &amp; anise flavors.</p></div>
  </div>

  <div class="section" style="top:542px">
    <h3 class="cat">Red Blend</h3>
    <div class="item" style="margin-bottom:10px"><div class="item-row"><span>2022 Riddle Blend - Napa - California</span><span class="g">$11</span><span class="b">$42</span></div><p class="note">A full bodied Syrah</p></div>
    <div class="item"><div class="item-row"><span>2022 Tall Timber /T.T. Reserve</span><span class="g"></span><span class="b">$48</span></div><p class="note">Blend of Petite Sirah &amp; Zinfandel.<br>Flavors of blackberry, violet, fig &amp; black prune.</p></div>
  </div>

  <p class="footer"><em>Enjoy 50% off bottled wines and sakes every Wednesday.</em><br>Bottle vintage subject to change.&nbsp; Corkage Fee: $15 per bottle<br>For each bottle purchased from our wine list,<br>we will waive one corkage fee.</p>
</section>

<section class="panel p4">
  <h2 class="panel-title">Sakes, Beers,<br>&amp; Non-Alcoholic</h2>

  <div class="section" style="top:87px">
    <div class="head-row"><h3 class="cat">House Sake</h3><span>Small $6</span><span>Large $10</span></div>
    <div class="pair" style="margin-top:6px"><span class="nm">Nakama</span><span>Small $7</span><span>Large $12</span></div>
    <p class="note" style="margin-left:9px">Sake mixed with sweet plum wine, served hot or cold.</p>
  </div>

  <div class="section" style="top:136px">
    <div class="head-row"><h3 class="cat">Plum Wine&nbsp; - 1.5 Liter</h3><span>Glass</span><span>Bottle</span></div>
    <div class="pair"><span class="nm">Hoshi</span><span>$ 9</span><span>$50</span></div>
    <p class="note" style="margin-left:9px">Fresh sweet taste. Well matured aroma from plum fruit</p>
  </div>

  <div class="section" style="top:179px">
    <h3 class="cat">Premium Cold Sakes and Sparking Sake</h3>
    <p class="sub">Small Bottle - 300ml</p>
    <div class="line"><span>Kaze Yama Organic - <i>Full, dry, fruity and balanced.</i></span><span class="b">$14</span></div>
    <div class="line"><span>Kaze Yama Nigori - <i>Unfiltered. sweet and fruity.<br>&nbsp;&nbsp;&nbsp;&nbsp;&nbsp;&nbsp;&nbsp;&nbsp;&nbsp;&nbsp;&nbsp;&nbsp;&nbsp;&nbsp;&nbsp;&nbsp;&nbsp;&nbsp;&nbsp;&nbsp;&nbsp;&nbsp;&nbsp;&nbsp;&nbsp;Notes of Cream &amp; Coconut.</i></span><span class="b">$16</span></div>
    <div class="line"><span>Winter Bloom Nigori - <i>Unfiltered. Flavors of Honey dew Melon<br>&nbsp;&nbsp;&nbsp;&nbsp;&nbsp;&nbsp;&nbsp;&nbsp;&nbsp;&nbsp;&nbsp;&nbsp;&nbsp;&nbsp;&nbsp;&nbsp;&nbsp;&nbsp;&nbsp;&nbsp;&nbsp;&nbsp;&nbsp;&nbsp;&amp; Pumpkin. Silky &amp; Smooth</i></span><span class="b">$18</span></div>
    <div class="line"><span>Soft Mist Nigori - <i>Unfiltered. Aromas of squash &amp; nuts.<br>&nbsp;&nbsp;&nbsp;&nbsp;&nbsp;&nbsp;&nbsp;&nbsp;&nbsp;&nbsp;&nbsp;&nbsp;&nbsp;&nbsp;&nbsp;&nbsp;&nbsp;&nbsp;&nbsp;&nbsp;&nbsp;&nbsp;&nbsp;&nbsp;&nbsp;&nbsp;&nbsp;&nbsp;&nbsp;&nbsp;&nbsp;Creamy &amp; dry</i></span><span class="b">$30</span></div>
    <div class="line"><span>Quiet Scholar - <i>Gentle flavors of pumpkin &amp; walnut.</i></span><span class="b">$32</span></div>
    <div class="line"><span>Sora Fizz - Sparkling Yuzu Sake Soda</span><span class="b">$18</span></div>
    <p class="sub">Large Bottle&nbsp; - 750ml</p>
    <div class="line"><span>Silver Heron - <i>Floral aroma. Silky and smooth.</i></span><span class="b">$32</span></div>
    <div class="line"><span>Morning Dew - <i>Floral aromas with clean flavors of honeydew &amp; lemon.</i></span><span class="b">$70</span></div>
  </div>

  <div class="section" style="top:357px">
    <h3 class="cat">1.5 Liter Bottle</h3>
    <div class="pair"><span class="nm">Kaze Yama Nigori</span><span>$ 9</span><span>$50</span></div>
    <p class="note" style="margin-left:9px">Unfiltered. sweet and fruity. Notes of Cream &amp; Coconut.</p>
  </div>

  <div class="section" style="top:403px">
    <h3 class="cat">On Draft</h3>
    <div class="pair" style="grid-template-columns:1fr 56px 58px"><span class="nm">Kaito Lager, Harbor Wheat,<br>Four Forks IPA, Timberline “IGA”</span><span>$7/Pint</span><span>$25/Pitcher</span></div>
    <div class="pair" style="grid-template-columns:1fr 56px 58px;margin-top:2px"><span class="nm">Coastline Cider</span><span>$5/Glass</span><span>$10/Pint</span></div>
    <p class="note" style="margin-left:9px">Varies with Seasonality - Please Ask Your Server</p>
  </div>

  <div class="section" style="top:473px">
    <h3 class="cat">Bottled Beers</h3>
    <div class="simple"><span>Belle Blonde</span><span class="b">$5</span></div>
    <div class="simple"><span>Red Barn, Red Barn Light</span><span class="b">$5</span></div>
    <div class="simple"><span>Groen 0.0 NA</span><span class="b">$5</span></div>
    <div class="simple"><span>Hopfield IPA NA</span><span class="b">$5</span></div>
    <div class="simple"><span>Hokuto</span><span class="b">$12</span></div>
  </div>

  <div class="section" style="top:562px">
    <h3 class="cat">Non-Alcoholic Beverages</h3>
    <div class="simple"><span>Alpina Sparkling Water</span><span class="b">$6</span></div>
    <div class="simple" style="line-height:9px;margin-top:2px"><span>Lemon-Lime, Cola, Diet Cola, Spiced Cola, Ginger Ale, Lemonade, Iced Tea<br><i style="font-size:5.8px">free refills</i></span><span class="b">$3</span></div>
    <div class="simple"><span>Cherry Spritz, Cola Grenadine</span><span class="b">$5</span></div>
    <div class="simple"><span>Orange Juice, Apple Juice, Cranberry Juice,</span><span class="b">$5</span></div>
    <div class="simple" style="line-height:12px"><span>Half &amp; Half Tea</span><span class="b">$5</span></div>
    <div class="simple" style="line-height:12px"><span>Hot Tea</span><span class="b">$3</span></div>
    <div class="simple" style="line-height:12px"><span>Fresh Brewed Coffee</span><span class="b">$3</span></div>
  </div>

  <p class="footer"><em>Enjoy 50% off bottled wines and sakes every Wednesday.</em><br>Bottle vintage subject to change.&nbsp; Corkage Fee: $15 per bottle<br>For each bottle purchased from our wine list,<br>we will waive one corkage fee.</p>
</section>

</body>
</html>
```